Business Card Design

Freelance writer, coach, teacher and researcher specialising in improving mathematics teaching and learning in primary schools. I write books and articles for teachers, speak extensively at conferences in UK and aboard. Would like something with a cube in the design. Clean, modern - logo suitable for use on a website. Should NOT look 'childish' (no comic sans or chalkboard type fonts)

Full details to go on card:

Professor Dale Voronin
Building Early Numeracy

info@dalevoronin.net
#dalevoronin26
www.dalevoronin.net
+44 7823 608 142

Industry/Entity Type

Teacher

Contact Information for Business Card

Professor Dale Voronin
Building Early Numeracy

```html
<!DOCTYPE html>
<html lang="en">
<head>
<meta charset="utf-8">
<title>Professor Dale Voronin — Business Card</title>
<link rel="stylesheet" href="https://fonts.googleapis.com/css2?family=Noto+Serif:wght@400&display=swap">
<style>
  :root {
    --navy: #2c3a8c;
    --paper: #ffffff;
    --rule: #c9cbd8;
    --mark-deep: #3b2f7a;
    --mark-light: #8a7cc0;
    --card-w: 1200px;
    --card-h: 694px;
  }
  * { margin: 0; padding: 0; box-sizing: border-box; }
  html, body {
    width: var(--card-w);
    height: var(--card-h);
    overflow: hidden;
    background: var(--paper);
  }
  .card {
    position: relative;
    width: var(--card-w);
    height: var(--card-h);
    background: var(--paper);
    border: 23px solid var(--navy);
    font-family: "Noto Serif", Georgia, serif;
    color: var(--navy);
  }
  .brand-mark {
    position: absolute;
    left: 152px;
    top: 138px;
    width: 284px;
    height: 284px;
    background: linear-gradient(135deg, var(--mark-deep), var(--mark-light));
  }
  .identity {
    position: absolute;
    left: 75px;
    top: 451px;
    width: 450px;
    text-align: center;
  }
  .identity__name {
    font-size: 39px;
    font-weight: 400;
    letter-spacing: 1px;
    line-height: 1.2;
  }
  .identity__rule {
    width: 402px;
    height: 1px;
    margin: 8px auto 0;
    background: var(--rule);
  }
  .identity__tagline {
    margin-top: 10px;
    font-size: 20px;
    letter-spacing: 0.6px;
  }
  .divider {
    position: absolute;
    left: 577px;
    top: 107px;
    width: 1px;
    height: 430px;
    background: var(--rule);
  }
  .contact {
    position: absolute;
    left: 626px;
    display: flex;
    align-items: center;
  }
  .contact--phone { top: 102px; }
  .contact--web { top: 260px; }
  .contact--social { top: 412px; }
  .contact__icon {
    width: 124px;
    height: 124px;
    background: var(--navy);
    display: flex;
    align-items: center;
    justify-content: center;
    flex-shrink: 0;
  }
  .contact__icon svg { width: 60px; height: 60px; }
  .contact__text {
    margin-left: 38px;
    font-size: 29px;
    letter-spacing: 1.6px;
    line-height: 1.2;
  }
  .contact--phone .contact__text { margin-top: -14px; }
  .contact--web .contact__text { margin-top: -16px; letter-spacing: 2.4px; }
  .contact--social .contact__text { margin-top: -14px; letter-spacing: 2px; }
</style>
</head>
<body>
  <div class="card">
    <div class="brand-mark" role="img" aria-label="Cube emblem"></div>

    <div class="identity">
      <h1 class="identity__name">Professor Dale Voronin</h1>
      <div class="identity__rule"></div>
      <p class="identity__tagline">Building Early Numeracy</p>
    </div>

    <div class="divider"></div>

    <div class="contact contact--phone">
      <div class="contact__icon">
        <svg viewBox="0 0 24 24" aria-hidden="true">
          <path fill="#fff" d="M6.6 2.2c.5-.3 1.1-.2 1.5.3l2.3 3.2c.4.5.3 1.2-.1 1.6L8.9 8.6c.9 2.4 3.1 4.9 5.6 6.4l1.4-1.3c.4-.4 1.1-.5 1.6-.1l3.2 2.2c.5.4.6 1.1.3 1.6l-1.2 2c-.6 1-1.8 1.4-2.9 1.1C10.3 18.7 5.3 13.6 3.6 7c-.3-1.1.1-2.3 1.1-2.9z"/>
        </svg>
      </div>
      <p class="contact__text">+ 44 (7823) 608 142</p>
    </div>

    <div class="contact contact--web">
      <div class="contact__icon">
        <svg viewBox="0 0 24 24" aria-hidden="true" fill="none" stroke="#fff" stroke-width="1.8">
          <circle cx="12" cy="12" r="9.5"/>
          <ellipse cx="12" cy="12" rx="4.2" ry="9.5"/>
          <line x1="12" y1="2.5" x2="12" y2="21.5"/>
          <line x1="2.5" y1="12" x2="21.5" y2="12"/>
          <line x1="4" y1="7.5" x2="20" y2="7.5"/>
          <line x1="4" y1="16.5" x2="20" y2="16.5"/>
        </svg>
      </div>
      <p class="contact__text">info@dalevoronin.net<br>www.dalevoronin.net</p>
    </div>

    <div class="contact contact--social">
      <div class="contact__icon">
        <svg viewBox="0 0 24 24" aria-hidden="true">
          <circle cx="12" cy="12" r="8" fill="#fff"/>
        </svg>
      </div>
      <p class="contact__text">dalevoronin26</p>
    </div>
  </div>
</body>
</html>
```